Fashion Label Startup Business Card Design

Marianne Velk is a startup fashion designer based on the Gold Coast in QLD Australia. Mariannes label " Sorrina by Velk " is based upon taking old world design techniques and infusing them modern twist. The card design should incorporate an old world theme using colours like mustard, ocha, black, white and elements of lace pattern.

Card Details:

Marianne Velk
Fashion Designer
P: 04 0163 5271
E: sorrinabyvelk@mailbrook.net
W: www.threadpage.net/SOrrinaByVelk

```html
<!DOCTYPE html>
<html lang="en">
<head>
<meta charset="utf-8">
<title>Marianne Velk — Business Card</title>
<link rel="stylesheet" href="https://fonts.googleapis.com/css2?family=Arvo:wght@700&family=Josefin+Slab:wght@400;600&display=swap">
<style>
  :root {
    --page-bg: #ecebe9;
    --card-taupe: #6e605e;
    --lace-white: #f1eeeb;
    --lace-soft: #cfc6c2;
    --lace-shadow: #a89c99;
    --panel-light: #dcdfde;
    --panel-pattern: #cdd2d1;
    --name-ink: #ece8e4;
    --contact-ink: #6e605e;
    --flourish-ink: #7d706e;
  }
  * { box-sizing: border-box; margin: 0; padding: 0; }
  html, body {
    width: 1200px;
    height: 900px;
    overflow: hidden;
    background: var(--page-bg);
  }
  .canvas {
    position: relative;
    width: 1200px;
    height: 900px;
  }
  .card {
    position: absolute;
    left: 320px;
    width: 560px;
    height: 320px;
    box-shadow: 0 6px 18px rgba(60, 50, 48, 0.18);
  }
  .card-front {
    top: 90px;
    background: var(--card-taupe);
    overflow: hidden;
  }
  .lace-band {
    position: absolute;
    top: 0;
    left: 0;
    width: 560px;
    height: 200px;
  }
  .front-title {
    position: absolute;
    left: 150px;
    top: 196px;
    display: flex;
    flex-direction: column;
    align-items: flex-end;
  }
  .designer-name {
    font-family: "Arvo", Georgia, serif;
    font-weight: 700;
    font-size: 40px;
    letter-spacing: 1.5px;
    color: var(--name-ink);
    line-height: 1.1;
    white-space: nowrap;
  }
  .designer-role {
    font-family: "Josefin Slab", Georgia, serif;
    font-weight: 400;
    font-size: 19px;
    color: var(--name-ink);
    margin-top: 4px;
    margin-right: 28px;
  }
  .card-back {
    top: 490px;
    background: var(--card-taupe);
    padding: 18px;
  }
  .back-panel {
    position: relative;
    width: 100%;
    height: 100%;
    border-radius: 8px;
    background:
      radial-gradient(circle at 22% 70%, var(--panel-pattern) 0 60px, transparent 61px),
      radial-gradient(circle at 80% 35%, var(--panel-pattern) 0 70px, transparent 71px),
      linear-gradient(135deg, var(--panel-light), var(--panel-pattern) 50%, var(--panel-light));
  }
  .contact-block {
    position: absolute;
    left: 0;
    right: 0;
    top: 92px;
    text-align: center;
    font-family: "Josefin Slab", Georgia, serif;
    font-weight: 600;
    font-size: 21px;
    line-height: 1.5;
    color: var(--contact-ink);
    list-style: none;
  }
  .flourish {
    position: absolute;
    width: 78px;
    height: 10px;
    border-radius: 5px;
    background: var(--flourish-ink);
    opacity: 0.6;
  }
  .flourish-top { left: 186px; top: 68px; }
  .flourish-bottom { left: 300px; top: 200px; }
</style>
</head>
<body>
<main class="canvas">
  <section class="card card-front" aria-label="Business card front">
    <svg class="lace-band" viewBox="0 0 560 200" role="img" aria-label="White lace border along the top edge, deeper on the left">
      <defs>
        <linearGradient id="laceTone" x1="0" y1="0" x2="1" y2="1">
          <stop offset="0" stop-color="#f1eeeb"/>
          <stop offset="0.55" stop-color="#cfc6c2"/>
          <stop offset="1" stop-color="#a89c99"/>
        </linearGradient>
      </defs>
      <path d="M0 0 H500 Q490 40 440 50 Q400 85 340 80 Q290 110 240 108 Q190 150 130 150 Q80 185 0 175 Z" fill="url(#laceTone)"/>
    </svg>
    <div class="front-title">
      <h1 class="designer-name">Marianne Velk</h1>
      <p class="designer-role">Fashion Designer</p>
    </div>
  </section>

  <section class="card card-back" aria-label="Business card back">
    <div class="back-panel" role="img" aria-label="Light grey paisley pattern background">
      <span class="flourish flourish-top" role="img" aria-label="Small decorative flourish"></span>
      <ul class="contact-block">
        <li>phone: 04 0163 5271</li>
        <li>sorrinabyvelk@mailbrook.net</li>
        <li>www.threadpage.net/SOrrinaByVelk</li>
      </ul>
      <span class="flourish flourish-bottom" role="img" aria-label="Small decorative flourish"></span>
    </div>
  </section>
</main>
</body>
</html>
```